Fishing charter business in Sitka Alaska needs new business card design

I have had the same design for 10 plus years, ready for something different. I have attached a copy of my current card and my website link is www.tidecrestangling.example
I am looking for something that will catch my clients eye, although I rely on word of mouth for most of my business a a nice business card will help people remember who I am. My business is located in Sitka Alaska, there are probably 20-30 other charter businesses in Sitka. I like the way my current card is laid out, with the two tone black and grey. I can leave it up to the designers to come up with something else.
Target Market(s)
men, women, couples. Anyone who likes fishing
Industry/Entity Type
Tourism
Contact Information for Business Card
Dorvane's Charter Service
Kelpline Bay Sportfishing
Colors
Designer to choose colors to be used in the design.
Requirements
Must have
- Lyle Dorvane
- PO Box 4716
- Sitka, AK 99835
- Compass Rose image
- 100 Ton USCG Licensed Captain
- ldorvane@wavenet.example
- 907-555-0148
- www.tidecrestangling.example
Nice to have
- ghost image of "boat helm"
Should not have
- be to complex

```html
<!DOCTYPE html>
<html lang="en">
<head>
<meta charset="utf-8">
<title>Lyle Dorvane – Business Card</title>
<link rel="stylesheet" href="https://fonts.googleapis.com/css2?family=Montserrat:wght@700&family=Open+Sans:wght@400;600;700&display=swap">
<style>
  :root {
    --page-bg: #f2f2f2;
    --card-bg: #ffffff;
    --brand-blue: #1273bb;
    --ink-dark: #2b2b2b;
    --ink-grey: #555555;
    --icon-grey: #8a8a8a;
  }
  * { margin: 0; padding: 0; box-sizing: border-box; }
  html, body {
    width: 1200px; height: 1200px; overflow: hidden;
    background: var(--page-bg);
  }
  .card {
    position: absolute; left: 50px; top: 277px;
    width: 1100px; height: 645px;
    background: var(--card-bg);
    font-family: "Open Sans", sans-serif;
    color: var(--ink-grey);
  }
  .compass-block {
    position: absolute; left: 0; top: 202px;
    width: 272px; height: 243px;
    background: var(--brand-blue);
  }
  .compass-rose {
    position: absolute; left: 66px; top: 51px;
    width: 140px; height: 140px; border-radius: 50%;
    background: radial-gradient(circle, rgba(255,255,255,0.55) 0%, rgba(255,255,255,0.2) 60%, rgba(255,255,255,0.05) 100%);
  }
  .contact-block { position: absolute; left: 584px; top: 0; }
  .name {
    position: absolute; top: 74px; left: 0; white-space: nowrap;
    font-family: "Montserrat", sans-serif; font-weight: 700;
    font-size: 50px; color: var(--brand-blue); letter-spacing: 0.5px;
  }
  .licence {
    position: absolute; top: 140px; left: 0; white-space: nowrap;
    font-size: 24px; font-weight: 600; color: var(--ink-dark);
  }
  .boat {
    position: absolute; top: 233px; left: 5px;
    width: 245px; height: 65px; border-radius: 40% 60% 45% 55% / 50%;
    background: linear-gradient(180deg, #d9d9d9 0%, #2e2e2e 55%, #9a9a9a 100%);
  }
  .business {
    position: absolute; top: 310px; left: 0; white-space: nowrap;
    font-size: 28px; font-weight: 700; line-height: 35px; color: var(--ink-grey);
  }
  .detail {
    position: absolute; left: 0; white-space: nowrap;
    font-size: 28px; line-height: 34px; display: flex; align-items: center;
  }
  .detail svg { width: 28px; height: 28px; margin-right: 18px; fill: var(--icon-grey); }
  .detail.address { top: 397px; }
  .detail.phone { top: 443px; font-weight: 700; }
  .detail.email { top: 490px; }
  .website {
    position: absolute; top: 568px; left: 0; width: 1100px;
    text-align: center; font-size: 25px; letter-spacing: 0.75em;
    color: var(--ink-grey); white-space: nowrap;
  }
</style>
</head>
<body>
  <div class="card">
    <div class="compass-block">
      <div class="compass-rose" role="img" aria-label="White compass rose emblem"></div>
    </div>

    <div class="contact-block">
      <h1 class="name">Lyle Dorvane</h1>
      <p class="licence">100 Ton USCG Licensed Captain</p>
      <div class="boat" role="img" aria-label="Side view of a black and white sport boat"></div>
      <p class="business">Dorvane's Charter Service<br>Kelpline Bay Sportfishing</p>

      <p class="detail address">
        <svg viewBox="0 0 24 24" aria-hidden="true"><path d="M12 2a7 7 0 0 0-7 7c0 5 7 13 7 13s7-8 7-13a7 7 0 0 0-7-7zm0 10a3 3 0 1 1 0-6 3 3 0 0 1 0 6z"/></svg>
        PO Box 4716 | Sitka, AK 99835
      </p>
      <p class="detail phone">
        <svg viewBox="0 0 24 24" aria-hidden="true"><rect x="1" y="1" width="22" height="22" rx="5"/><path fill="#fff" d="M8.5 5.5l2 3-1.3 1.3a8 8 0 0 0 5 5l1.3-1.3 3 2-1.2 2.3c-5.5 0-10.6-5.1-10.6-10.6z"/></svg>
        907-555-0148
      </p>
      <p class="detail email">
        <svg viewBox="0 0 24 24" aria-hidden="true"><path d="M2 5h20v14H2z M2 5l10 8 10-8" stroke="#fff" stroke-width="1.5"/></svg>
        ldorvane@wavenet.example
      </p>
    </div>

    <p class="website">www.tidecrestangling.example</p>
  </div>
</body>
</html>
```